Want to incorporate elements of all these items to make an amazing sign to welcome people to the community. The sign is 6x4 and needs to incorporate the following items:

Welcome to Corwick Meadows

Come visit the PRD sales center at 745 thistledown road
High Speed Fiber Internet
Land financing starting at $299 (No credit checks)
Let us build your dream home!
555-284-7390
We like the gold and black design no teal or blue that was another agents design. Some combination of the current sign all the stuff listed above and then design elements that tie into the truck wrap.

Target Market(s)

People visiting the neighborhood

Industry/Entity Type

real estate and construction

Font styles to use
Serif

Colors

Designer to choose colors to be used in the design.

Requirements
Must have
• PRD Home Builders Welcomes you to Corwick Meadows, Let us build your dream home, Phone number, Land financing starting at $299 NO credit checks

```html
<!DOCTYPE html>
<html lang="en">
<head>
<meta charset="utf-8">
<title>Welcome to Corwick Meadows</title>
<link rel="stylesheet" href="https://fonts.googleapis.com/css2?family=Great+Vibes&family=League+Gothic&family=Montserrat:wght@700;800&display=swap">
<style>
  :root {
    --gold: #d9b036;
    --black: #000000;
    --white: #ffffff;
  }
  html, body {
    margin: 0;
    padding: 0;
    width: 1200px;
    height: 819px;
    overflow: hidden;
    background: var(--black);
  }
  .sign {
    position: relative;
    width: 1200px;
    height: 819px;
    background: var(--black);
    overflow: hidden;
    color: var(--white);
  }
  .condensed {
    font-family: "League Gothic", "Oswald", sans-serif;
    font-weight: 400;
    text-transform: uppercase;
    line-height: 1;
    white-space: nowrap;
  }
  .title-tab {
    position: absolute;
    left: 262px;
    top: 0;
    width: 675px;
    height: 197px;
    background: var(--gold);
    text-align: center;
  }
  .title-tab__script {
    position: absolute;
    left: 0; right: 0;
    top: 12px;
    font-family: "Great Vibes", cursive;
    font-size: 90px;
    line-height: 1;
    color: var(--white);
  }
  .title-tab__name {
    position: absolute;
    left: 0; right: 0;
    top: 114px;
    font-family: "Montserrat", sans-serif;
    font-weight: 800;
    font-size: 50px;
    line-height: 1;
    white-space: nowrap;
    color: var(--white);
  }
  .visit {
    position: absolute;
    left: 0; right: 0;
    top: 230px;
    text-align: center;
    font-size: 58px;
  }
  .address {
    position: absolute;
    left: 0; right: 0;
    top: 288px;
    display: flex;
    justify-content: center;
    align-items: center;
    gap: 22px;
  }
  .address__pin { width: 30px; height: 42px; }
  .address__text {
    font-size: 94px;
    color: var(--gold);
  }
  .feature-band {
    position: absolute;
    left: 0; right: 0;
    top: 388px;
    height: 92px;
    background: var(--gold);
    display: flex;
    align-items: center;
    justify-content: center;
    font-family: "Montserrat", sans-serif;
    font-weight: 700;
    font-size: 49px;
    letter-spacing: 0.5px;
    white-space: nowrap;
  }
  .financing {
    position: absolute;
    left: 0; right: 0;
    top: 494px;
    text-align: center;
    font-size: 78px;
    color: var(--gold);
  }
  .price {
    position: absolute;
    left: 531px;
    top: 565px;
    width: 136px;
    height: 86px;
    border-radius: 18px;
    background: var(--gold);
    display: flex;
    align-items: center;
    justify-content: center;
    font-size: 80px;
    padding-top: 4px;
    box-sizing: border-box;
  }
  .no-credit {
    position: absolute;
    left: 0; right: 0;
    top: 664px;
    text-align: center;
    font-size: 52px;
  }
  .footer-band {
    position: absolute;
    left: 0; right: 0;
    top: 726px;
    height: 93px;
    background: var(--gold);
  }
  .footer-band__tagline {
    position: absolute;
    left: 54px;
    top: 22px;
    font-size: 60px;
  }
  .footer-band__phone {
    position: absolute;
    left: 656px;
    top: 16px;
    display: flex;
    align-items: center;
    gap: 14px;
  }
  .footer-band__phone svg { width: 44px; height: 44px; }
  .footer-band__number {
    font-family: "Montserrat", sans-serif;
    font-weight: 700;
    font-size: 62px;
    line-height: 1;
    white-space: nowrap;
  }
</style>
</head>
<body>
<main class="sign">
  <header class="title-tab">
    <div class="title-tab__script">Welcome to</div>
    <div class="title-tab__name">CORWICK MEADOWS</div>
  </header>

  <div class="visit condensed">Come visit the PRD sales center at</div>
  <div class="address">
    <svg class="address__pin" viewBox="0 0 30 42" aria-hidden="true">
      <path d="M15 0C6.7 0 0 6.7 0 15c0 9 15 27 15 27s15-18 15-27C30 6.7 23.3 0 15 0z" fill="#fff"/>
      <circle cx="15" cy="14" r="6" fill="#000"/>
    </svg>
    <span class="address__text condensed">745 Thistledown Road</span>
  </div>

  <div class="feature-band">HIGH SPEED FIBER INTERNET</div>

  <div class="financing condensed">Land financing starting at</div>
  <div class="price condensed">$299</div>
  <div class="no-credit condensed">(No credit checks)</div>

  <footer class="footer-band">
    <div class="footer-band__tagline condensed">Let us build your dream home!</div>
    <div class="footer-band__phone">
      <svg viewBox="0 0 44 44" aria-hidden="true">
        <path d="M9 6c2-1 4 0 5 2l3 6c1 2 0 3-1 4l-2 2c1 4 5 8 9 10l2-2c1-1 3-2 4-1l6 3c2 1 3 3 2 5l-2 3c-2 2-5 2-8 1C16 35 8 27 5 16c-1-3 0-6 2-8z" fill="none" stroke="#fff" stroke-width="3"/>
        <path d="M25 10a10 10 0 0 1 9 9M25 4a16 16 0 0 1 15 15M25 16a4 4 0 0 1 3 3" fill="none" stroke="#fff" stroke-width="2.5" stroke-linecap="round"/>
      </svg>
      <span class="footer-band__number">555-284-7390</span>
    </div>
  </footer>
</main>
</body>
</html>
```